Beautiful, sharp, website design for family-run property development company.

We are property developers in Kent (south east of London) who want to see the local town change. We are the only local property developer that is a family run business, focussing primarily on converting old, dilapidated Victorian buildings into beautiful residential spaces. Unlike other national developers, we work to regenerate buildings to create new employment opportunities, housing, and revive the town Centre .

Target Market(s)

1. Investors and Joint Venture partners - people with money to invest in property
2. Buyers of property - 25 to 40 year old, young professionals.
3. Commercial funders (people lending money to our projects
4. Professional team: Architects, builders, Estate agent who want to work with us

Industry/Entity Type

Real Estate Development

Coding

Number of Pages Required

Font styles to use
Other font styles liked:
• Please follow the brief of stylish, elegant, modern

Colors

Designer to choose colors to be used in the design.

Requirements
Must have
• Please use these websites as a reference of what we are looking to achieve.
• http://brellmoorhomes.com/#page5
• https://fernwick.co.uk/
• http://ambertide.co.uk/
• http://www.theharroweyestates.co.uk/about-harrowey
• Clean, simple, elegant, minimal design.
• Images of interiors of houses that have been converted from old buildings
• Images of farm buildings e.g. barns that have been converted to new homes or offices. Images of properties that may have been an old factory or old commercial property that is now a trendy apartment.
• Please use images of properties and interiors that are from the South East of England (including Kent, Surrey, Sussex, Hampshire, Dorset). There is a distinct style of housing in this part of England.
Nice to have
• Colours consistent with our brand colour palette (attached)

```html
<!DOCTYPE html>
<html lang="en">
<head>
<meta charset="utf-8">
<title>Oakvale Row Homes</title>
<link rel="stylesheet" href="https://fonts.googleapis.com/css2?family=Montserrat:wght@400;500;600;700&display=swap">
<style>
:root{
  --ink:#1e1e1e;
  --sage:#6b7f78;
  --sage-dark:#637670;
  --sage-light:#b9c6c1;
  --mist:#f2f2f2;
  --panel:#eff4ec;
  --charcoal:#222725;
  --footer:#262626;
  --white:#ffffff;
}
*{margin:0;padding:0;box-sizing:border-box}
html,body{width:1200px;height:2748px;overflow:hidden}
body{font-family:'Montserrat',sans-serif;color:var(--ink);background:var(--white);position:relative}
.btn{position:absolute;background:var(--ink);color:var(--white);border-radius:22px;font-size:18px;font-weight:500;display:flex;align-items:center;justify-content:center;letter-spacing:.3px}
.underline{position:absolute;height:4px;background:var(--sage)}

/* header */
.site-header{position:absolute;left:0;top:0;width:1200px;height:137px;background:var(--mist)}
.brand{position:absolute;left:150px;top:52px;display:flex;align-items:center;gap:12px;font-size:24px;font-weight:500;color:var(--sage);letter-spacing:1px}
.brand-dot{width:14px;height:14px;background:var(--sage)}
.nav{position:absolute;top:60px;font-size:20px;font-weight:500;letter-spacing:1px}

/* hero */
.hero{position:absolute;left:0;top:137px;width:1200px;height:453px}
.hero-photo{position:absolute;inset:0;background:linear-gradient(100deg,#c9d3d1 0%,#d6dedc 45%,#c3cccb 75%,#aab4b3 100%)}
.hero-title{position:absolute;left:611px;top:218px;font-size:50px;font-weight:400;letter-spacing:2px;line-height:1}
.hero-title-strong{position:absolute;left:611px;top:278px;font-size:52px;font-weight:700;letter-spacing:3px;line-height:1}
.hero-text{position:absolute;left:621px;top:357px;width:540px;font-size:18px;line-height:21.5px;letter-spacing:.6px}

/* intro */
.intro-heading{position:absolute;left:53px;top:668px;font-size:27px;font-weight:600;letter-spacing:2px;line-height:33px}
.intro-heading span{color:var(--sage);font-weight:700}
.intro-text{position:absolute;left:51px;top:767px;width:600px;font-size:17px;line-height:21.5px;letter-spacing:.5px}
.intro-photo{position:absolute;left:734px;top:661px;width:376px;height:249px;background:linear-gradient(180deg,#e9e9e6 0%,#dcdad4 55%,#c58f58 80%,#b27a45 100%);box-shadow:0 18px 30px rgba(0,0,0,.18)}

/* motive */
.motive{position:absolute;left:0;top:978px;width:1200px;height:374px;background:var(--charcoal)}
.tile{position:absolute;width:175px;height:160px}
.motive-title{position:absolute;left:577px;top:1040px;font-size:37px;font-weight:600;letter-spacing:3px;color:var(--white)}
.motive-title span{color:var(--sage-light)}
.motive-text{position:absolute;left:582px;top:1113px;width:500px;font-size:19px;line-height:23.5px;color:var(--white);letter-spacing:.5px;font-weight:500}
.region{position:absolute;font-size:23px;color:var(--white);letter-spacing:1px}

/* services */
.service-photo{position:absolute;width:373px;height:241px}
.service-panel{position:absolute;width:370px;height:243px;background:var(--panel)}
.service-title{position:absolute;font-size:20px;font-weight:600;letter-spacing:2px;line-height:26px}
.service-title span{color:var(--sage);font-weight:700}
.service-text{position:absolute;width:318px;font-size:12px;line-height:14.5px;letter-spacing:.3px}

/* quote */
.quote-band{position:absolute;left:0;top:1917px;width:1200px;height:329px;background:var(--sage-dark)}
.quote{position:absolute;left:40px;top:2025px;width:1120px;text-align:center;color:var(--white);font-size:28px;font-weight:500;letter-spacing:1.6px;line-height:34px}

/* partners */
.partner{position:absolute;top:2303px;height:88px;background:#d9dedc;border-radius:44px}

/* footer */
.site-footer{position:absolute;left:0;top:2459px;width:1200px;height:289px;background:var(--footer)}
.footer-brand{position:absolute;left:32px;top:2616px;display:flex;align-items:center;gap:12px;font-size:30px;font-weight:500;color:var(--sage);letter-spacing:1px}
.footer-heading{position:absolute;left:403px;top:2525px;font-size:28px;font-weight:500;letter-spacing:2.5px;color:var(--white)}
.footer-text{position:absolute;left:397px;top:2600px;width:330px;font-size:16.5px;line-height:20.5px;font-weight:500;letter-spacing:.4px;color:var(--white)}
.contact{position:absolute;left:846px;font-size:20px;letter-spacing:1.2px;color:var(--white)}
.icon{position:absolute}
</style>
</head>
<body>

<header class="site-header">
  <div class="brand"><span class="brand-dot"></span>OAKVALE ROW HOMES</div>
  <nav>
    <span class="nav" style="left:704px">HOME</span>
    <span class="nav" style="left:797px">PROJECTS</span>
    <span class="nav" style="left:941px">ABOUT</span>
    <span class="nav" style="left:1053px">CONTACT</span>
  </nav>
</header>

<section class="hero">
  <div class="hero-photo" role="img" aria-label="Bright modern kitchen interior in soft pale tones"></div>
</section>
<h1 class="hero-title">Redesign Your</h1>
<div class="hero-title-strong">PROPERTY</div>
<div class="underline" style="left:622px;top:331px;width:141px"></div>
<p class="hero-text">At Oakvale Row we develop beautiful and unique properties in and around South London.We strive for perfection and never stop challenging ourselves.</p>
<div class="btn" style="left:624px;top:437px;width:144px;height:43px">View More</div>

<h2 class="intro-heading">PROPERTY DEVELOPERS IN<br><span>SOUTH (East of London)</span></h2>
<div class="underline" style="left:53px;top:734px;width:184px"></div>
<p class="intro-text">We’ve been developing properties in and around South London for the last 4 years. We are a small team of dedicated professionals and we ensure that our exacting standards are .met throughout the whol design and build process</p>
<div class="btn" style="left:50px;top:877px;width:144px;height:42px">View More</div>
<div class="intro-photo" role="img" aria-label="Converted living room with oak flooring and white sofa"></div>

<section class="motive"></section>
<div class="tile" style="left:71px;top:999px;background:linear-gradient(180deg,#9bb3cf 0%,#b96e4c 30%,#8e6a52 70%,#5f7a3f 100%)" role="img" aria-label="Brick and flint detached house"></div>
<div class="tile" style="left:256px;top:998px;background:linear-gradient(180deg,#b7cde6 0%,#b8613f 40%,#a4553a 70%,#6c8f45 100%)" role="img" aria-label="New red brick family home with lawn"></div>
<div class="tile" style="left:73px;top:1168px;height:157px;background:linear-gradient(180deg,#c2d3e4 0%,#bd6a44 35%,#9e4f35 70%,#b5342c 100%)" role="img" aria-label="Brick townhouses with flower beds"></div>
<div class="tile" style="left:255px;top:1168px;height:157px;background:linear-gradient(180deg,#a7c6e6 0%,#e6e1d6 40%,#5b4a3e 70%,#8c8a86 100%)" role="img" aria-label="Tudor style timber framed houses"></div>
<h2 class="motive-title">OUR BUSINESS <span>MOTIVE</span></h2>
<div class="underline" style="left:581px;top:1082px;width:184px;background:var(--sage-light)"></div>
<p class="motive-text">we work to regenerate buildings to create new employment opportunities, housing, and revive the town Centre Target Market(s) like :</p>
<span class="region" style="left:613px;top:1215px">Kent</span>
<span class="region" style="left:775px;top:1215px">Surrey</span>
<span class="region" style="left:612px;top:1254px">Dorset</span>
<span class="region" style="left:773px;top:1254px">Sussex</span>

<div class="service-photo" style="left:246px;top:1394px;background:linear-gradient(180deg,#ecebe8 0%,#ddd6cc 50%,#c7b8a4 100%)" role="img" aria-label="Open plan living room with floating staircase"></div>
<div class="service-panel" style="left:619px;top:1394px"></div>
<h3 class="service-title" style="left:652px;top:1444px">INTERIOR<br><span>DESIGN</span></h3>
<div class="underline" style="left:652px;top:1494px;width:54px;height:3px;background:var(--ink)"></div>
<p class="service-text" style="left:650px;top:1522px">We’ve been developing properties in and around South London for the last 4 years. We are a small team of dedicated professionals</p>

<div class="service-panel" style="left:246px;top:1637px;width:373px"></div>
<h3 class="service-title" style="left:279px;top:1687px">STRUCTURE<br><span>DESIGN</span></h3>
<div class="underline" style="left:279px;top:1737px;width:54px;height:3px;background:var(--ink)"></div>
<p class="service-text" style="left:277px;top:1764px">We’ve been developing properties in and around South London for the last 4 years. We are a small team of dedicated professionals</p>
<div class="service-photo" style="left:619px;top:1637px;width:370px;height:243px;background:linear-gradient(180deg,#ecebe8 0%,#ddd6cc 50%,#c7b8a4 100%)" role="img" aria-label="Living area with staircase and kitchen beyond"></div>

<section class="quote-band"></section>
<blockquote class="quote">“We are the only local property developer that is a family run business, focussing primarily on converting old, dilapidated Victorian buildings into beautiful residential spaces”</blockquote>

<div class="partner" style="left:74px;width:164px"></div>
<div class="partner" style="left:277px;width:220px;border-radius:8px"></div>
<div class="partner" style="left:537px;width:162px"></div>
<div class="partner" style="left:743px;width:168px"></div>
<div class="partner" style="left:959px;width:180px;border-radius:8px"></div>

<footer class="site-footer"></footer>
<div class="footer-brand"><span class="brand-dot" style="width:18px;height:18px"></span>OAKVALE ROW</div>
<h2 class="footer-heading">ABOUT US</h2>
<p class="footer-text">We are property developers in Kent (south east of London) who want to see the local town change.</p>

<svg class="icon" style="left:794px;top:2527px" width="36" height="26" viewBox="0 0 36 26"><rect x="1" y="1" width="34" height="24" fill="#b9c6c1"/><path d="M1 1 L18 15 L35 1 M1 25 L14 12 M35 25 L22 12" stroke="#262626" stroke-width="2" fill="none"/></svg>
<span class="contact" style="top:2527px">hello@oakvalerow.co.uk</span>
<svg class="icon" style="left:799px;top:2575px" width="28" height="38" viewBox="0 0 28 38"><path d="M14 1 C6 1 1 7 1 14 C1 24 14 37 14 37 C14 37 27 24 27 14 C27 7 22 1 14 1Z" fill="#b9c6c1"/><circle cx="14" cy="14" r="5" fill="#262626"/></svg>
<span class="contact" style="top:2582px">12 Orchard Lane, Ashford</span>
<svg class="icon" style="left:803px;top:2636px" width="34" height="34" viewBox="0 0 34 34"><path d="M8 2 L13 10 L10 14 C12 19 15 22 20 24 L24 21 L32 26 L29 32 C15 32 2 19 2 5 Z" fill="#b9c6c1"/></svg>
<span class="contact" style="top:2642px">01632 960418</span>

</body>
</html>
```